Medical Centre Website

We need a new design for a medical centre based in Perth, Western Australia called 'Tarvin Grove Medical Centre'.

The medical centre does general practitioner work including general checkups, ecg, heart checks, woman's health and more servicing children and adults. They also do home visits on occasions where the patient cannot attend the centre.

They would like an information/brochure website where visitors can read up on the practice, send email and view their location.

The client wish the design to be clean, fresh and light. The main colours are a light purple/blue and to a dark navy blue. The client would not want the logo to be altered in any way. This includes changing the words colours or the image.

The final design should represent a loving, family friendly practice where patients can come to receive the best treatments.

We just need the end product to be presented to un in a layed psd format. The fonts must be as per the W3C standards.

**IMPORTANT**
I have received heaps of chatlink invites in the past. To treat everyone fairly, I do not add people to my chatlink list as in the past people expected us to give them the prize. If you have questions, please ask them in pixel forum as it may benefit others who are also designing the site. If I need to, I will send a message to the user.
Updates

Hi Designers,

Most designs we have received have been overly cluttered. Are you able to simplify the designs.

Cheers, Dorian

Hi Designers,

Some of the designs are quite attractive but aremore cluttered than I would like. If you have a look at the following design, the design is very simple and straight to the point. A lot of designs have too much wording and the reader can be put off. We are looking something more like:

velmoxa.com.au

I would prefer to see designs and have opened up the contest for a further 7 days.

Designers,

We have received feedback from the client and Quite frankly he don’t really like any of them.They are too cluttered and Americanised. All drab blue colours.
 
If you have a look at template monster, these designs are better and cleaner. We do not want heaps of writing on the front page.

If you look at the eariler examples such as quorbeyclinic.com.au which I did myself, the client loves that simplicity of the site.

```html
<!DOCTYPE html>
<html lang="en">
<head>
<meta charset="utf-8">
<title>Tarvin Grove Medical Centre</title>
<link href="https://fonts.googleapis.com/css2?family=Arimo:wght@400;700&family=Roboto+Condensed:wght@300;400&display=swap" rel="stylesheet">
<style>
:root{
  --lavender:#95a6d6;
  --lavender-text:#8f9fd6;
  --logo-blue:#1f4ea3;
  --charcoal:#3a3a3a;
  --tab-grey:#e5e5e5;
  --stripe-grey:#d0d0d0;
  --border:#d3d3d3;
  --text:#444;
  --muted:#777;
  --band-top:#ffffff;
  --band-bottom:#e6e9f4;
}
*{margin:0;padding:0;box-sizing:border-box}
html,body{width:1200px;height:1000px;overflow:hidden}
body{position:relative;background:#fff;font-family:"Arimo",Arial,sans-serif;color:var(--text)}
.top-band{position:absolute;left:0;top:0;width:1200px;height:396px;background:linear-gradient(var(--band-top) 0%,#f3f5fa 40%,var(--band-bottom) 100%)}

.brand{position:absolute;left:99px;top:36px;color:var(--logo-blue);font-weight:400;display:flex;align-items:center;gap:12px}
.brand-mark{width:14px;height:14px;border-radius:50%;background:var(--logo-blue)}
.brand-name{font-size:28px;line-height:30px;letter-spacing:.3px}
.brand-sub{display:block;font-size:14px;line-height:18px;letter-spacing:2.5px;margin-top:2px;padding-left:112px}

.phone{position:absolute;left:943px;top:61px;display:flex;align-items:center;gap:12px;font-family:"Roboto Condensed",Arial,sans-serif;font-size:21px;color:#333}

.hero-frame{position:absolute;left:99px;top:112px;width:998px;height:355px;background:#fff;border:1px solid var(--border)}
.main-nav{position:absolute;left:9px;top:9px;width:977px;height:46px;background:var(--charcoal);display:flex}
.main-nav a{color:#fff;text-decoration:none;font-size:12.5px;display:flex;align-items:center;justify-content:center;border-right:1px solid #555;height:46px}
.main-nav a.is-active{background:var(--lavender);color:#111;border-right:none}
.hero{position:absolute;left:9px;top:55px;width:977px;height:290px;background:
  radial-gradient(ellipse at 75% 45%,#a9bfe6 0%,#6f8fcb 30%,transparent 60%),
  linear-gradient(100deg,#1d3870 0%,#2f5aa6 35%,#4f7dc6 55%,#28497f 100%)}
.hero-caption{position:absolute;left:58px;top:100px;color:#fff;font-size:15.5px}
.hero-more{position:absolute;left:58px;top:142px;color:#fff;font-size:12.5px;text-decoration:underline}
.hero-dots{position:absolute;left:466px;top:268px;display:flex;gap:3px}
.hero-dots span{width:10px;height:10px;border-radius:50%;background:#fff}
.hero-dots span.is-current{background:var(--charcoal)}

.service-tabs{position:absolute;left:99px;top:472px;width:335px;height:354px}
.service-tabs svg{position:absolute;left:0;top:0}
.service-tab{position:absolute;left:25px}
.service-tab h3{font-weight:400;font-size:14px;color:#333}
.service-tab p{font-size:10.5px;line-height:12.5px;color:#555;margin-top:10px}
.service-tab.is-active h3,.service-tab.is-active p{color:#fff}

.content{position:absolute;left:438px;top:491px;width:430px}
.content h2{font-weight:400;font-size:14px;color:#444}
.content p{font-size:10.5px;line-height:15px;color:#555}
.content .intro{margin-top:42px}
.content .intro + p{margin-top:15px}
.family-photo{position:absolute;left:438px;top:672px;width:97px;height:100px;background:linear-gradient(135deg,#e9d8cf,#b08670 55%,#f2ece8)}
.feature-text{position:absolute;left:570px;top:672px;width:300px;font-size:10.5px;line-height:15px;color:#555}

.hours{position:absolute;left:912px;top:472px;width:186px;height:180px;border:1px solid var(--border);background:#fff}
.hours svg{position:absolute;left:0;top:0}
.hours h4{position:absolute;left:0;right:0;top:21px;text-align:center;font-weight:400;font-size:15.5px;color:#333}
.hours hr{position:absolute;left:14px;top:48px;width:156px;border:none;border-top:1px solid #e4e4e4}
.hours ul{position:absolute;left:30px;top:66px;list-style:none;font-size:12px;color:#444}
.hours li{height:24px}

.share{position:absolute;left:912px;top:665px;width:185px;height:36px;border:1px solid var(--border);display:flex;align-items:center;justify-content:space-between;padding:0 13px 0 12px;font-family:"Roboto Condensed",Arial,sans-serif;font-weight:300;font-size:15px;color:var(--lavender-text)}

.footer{position:absolute;left:99px;top:914px;width:1034px;border-top:1px solid #d6d6d6}
.footer-links{margin-top:15px;font-size:10px;font-weight:700;color:#666}
.footer-links span{margin:0 6px}
.copyright{margin-top:10px;font-size:10px;color:#777}
.social{position:absolute;right:0;top:12px;display:flex;gap:8px}
.social span{width:27px;height:27px;border-radius:50%;background:radial-gradient(circle at 40% 35%,#b5b5b5,#6d6d6d)}
</style>
</head>
<body>
<div class="top-band"></div>

<header>
  <div class="brand">
    <div>
      <span class="brand-name">Tarvin Grove</span>
      <span class="brand-sub">MEDICAL CENTRE</span>
    </div>
    <span class="brand-mark"></span>
  </div>
  <div class="phone">
    <svg width="22" height="22" viewBox="0 0 22 22" aria-hidden="true">
      <circle cx="11" cy="11" r="10" fill="none" stroke="#333" stroke-width="1.6"/>
      <path d="M7.5 6.2c.6-.5 1.3-.4 1.6.2l.9 1.8c.2.5 0 .9-.4 1.2l-.6.4c.5 1.2 1.4 2.2 2.6 2.8l.5-.6c.3-.4.8-.5 1.2-.3l1.8 1c.5.3.6 1 .1 1.5l-.8.8c-.7.7-2 .7-3.4-.1-2-1.2-3.6-3-4.4-5-.5-1.3-.3-2.3.3-3z" fill="#333"/>
    </svg>
    <span>123 456 70120</span>
  </div>
</header>

<section class="hero-frame">
  <nav class="main-nav">
    <a href="#" class="is-active" style="width:145px">Home</a>
    <a href="#" style="width:118px">About Us</a>
    <a href="#" style="width:137px">Our Services</a>
    <a href="#" style="width:121px">Health</a>
    <a href="#" style="width:135px">Appointment</a>
    <a href="#" style="width:142px;border-right:none">Contact Us</a>
  </nav>
  <div class="hero" role="img" aria-label="Blue-toned photo of a stethoscope resting on an open book">
    <p class="hero-caption">Lorem Ipsum is simply dummy text of the printing</p>
    <a class="hero-more">+read more</a>
    <div class="hero-dots"><span class="is-current"></span><span></span><span></span><span></span></div>
  </div>
</section>

<section class="service-tabs">
  <svg width="335" height="354" viewBox="0 0 335 354" aria-hidden="true">
    <path d="M0 0H321Q295 40 273 83H0Z" fill="var(--charcoal)"/>
    <rect x="0" y="0" width="8" height="83" fill="var(--lavender)"/>
    <path d="M0 91H269Q256 130 253 173H0Z" fill="var(--tab-grey)"/>
    <rect x="0" y="91" width="8" height="82" fill="var(--stripe-grey)"/>
    <path d="M0 180H253Q252 222 257 263H0Z" fill="var(--tab-grey)"/>
    <rect x="0" y="180" width="8" height="83" fill="var(--stripe-grey)"/>
    <path d="M0 270H275Q295 320 331 353H0Z" fill="var(--tab-grey)"/>
    <rect x="0" y="270" width="8" height="83" fill="var(--stripe-grey)"/>
  </svg>
  <div class="service-tab is-active" style="top:20px"><h3>General Checkups</h3><p>Lorem Ipsum is simply dummy text of the printing<br>and typesetting industry</p></div>
  <div class="service-tab" style="top:117px"><h3>ECG</h3><p>Lorem Ipsum is simply dummy text of</p></div>
  <div class="service-tab" style="top:206px"><h3>Heart Checks</h3><p>Lorem Ipsum is simply dummy text of</p></div>
  <div class="service-tab" style="top:296px;left:24px"><h3>Womens Health</h3><p>Lorem Ipsum is simply dummy text of</p></div>
</section>

<main class="content">
  <h2>General Checkups</h2>
  <p class="intro">Lorem Ipsum is simply dummy text of the printing and typesetting industry. Lorem Ipsum has been the industry's standard dummy text ever since the 1500s, when an unknown printer took a galley of type and scrambled it to make a type specimen book.</p>
  <p>Lorem Ipsum is simply dummy text of the printing and typesetting industry. Lorem Ipsum has been the industry's standard dummy</p>
</main>
<div class="family-photo" role="img" aria-label="Photo of a smiling mother hugging her young daughter"></div>
<p class="feature-text">Lorem Ipsum is simply dummy text of the printing and typesetting industry. Lorem Ipsum has been the industry's standard dummy text ever since the 1500s, when an unknown</p>

<aside>
  <div class="hours">
    <svg width="186" height="180" viewBox="0 0 186 180" aria-hidden="true">
      <path d="M0 2H49L0 35Z" fill="var(--lavender)"/>
      <path d="M184 144V177H135Z" fill="var(--lavender)"/>
    </svg>
    <h4>Practice Hours</h4>
    <hr>
    <ul>
      <li>Mon-Fri 9.00am-8.00pm</li>
      <li>Saturday 9.00am-8.00pm</li>
      <li>Sunday 9.00am-8.00pm</li>
    </ul>
  </div>
  <div class="share">
    <span>+ SHARE THIS PAGE</span>
    <svg width="22" height="22" viewBox="0 0 22 22" aria-hidden="true">
      <line x1="5" y1="11" x2="17" y2="4" stroke="#777" stroke-width="2"/>
      <line x1="5" y1="11" x2="17" y2="18" stroke="#777" stroke-width="2"/>
      <circle cx="5" cy="11" r="3.5" fill="#777"/>
      <circle cx="17" cy="4" r="3.5" fill="#777"/>
      <circle cx="17" cy="18" r="3.5" fill="#777"/>
    </svg>
  </div>
</aside>

<footer class="footer">
  <p class="footer-links">Lorem Ipsum<span>|</span>Lorem Ipsum<span>|</span>Lorem Ipsum</p>
  <p class="copyright">Copyright All Right Reserved. Tarvin Grove.</p>
  <div class="social"><span></span><span></span><span></span></div>
</footer>
</body>
</html>
```